Investment Advisor E-Newsletter Banner Design

I need a banner designed for an email newsletter that will be sent monthly to clients and prospects. We want to see designs that are elegant and use our logo well. The banner should be 922x150px and should go well with the www.bhtlwest.com website. Should include Logo and email and phone number.

Target Market(s)

High net worth investors

Number of Pages Required

1 page

Requirements
Must have
• logo, place for email (info@bhtlwest.com) and phone number (555-219-0387), colors and design that work well with www.bhtlwest.com website

```html
<!DOCTYPE html>
<html lang="en">
<head>
<meta charset="utf-8">
<title>Bayhill Trust West Advisors – Newsletter Banner</title>
<link rel="stylesheet" href="https://fonts.googleapis.com/css2?family=Cormorant+Garamond:ital,wght@0,500;1,500&display=swap">
<style>
  :root {
    --brand-blue: #1c1c9c;
    --phone-blue: #1a2fa8;
    --text-grey: #555555;
    --icon-dark: #3a3a3a;
    --icon-light: #6fa8d8;
    --bg-light: #f6f6f6;
    --bg-mid: #dcdcdc;
    --bg-warm: #d9c9a0;
  }
  html, body {
    margin: 0;
    padding: 0;
    width: 1200px;
    height: 195px;
    overflow: hidden;
    background: #ffffff;
  }
  .banner {
    position: relative;
    width: 1200px;
    height: 195px;
    overflow: hidden;
    font-family: "Cormorant Garamond", Georgia, serif;
  }
  .banner-backdrop {
    position: absolute;
    inset: 0;
    background:
      radial-gradient(ellipse 260px 200px at 470px 20px, rgba(217, 201, 160, 0.55), rgba(217, 201, 160, 0) 70%),
      radial-gradient(ellipse 700px 420px at 520px 90px, var(--bg-mid), rgba(220, 220, 220, 0) 75%),
      linear-gradient(90deg, var(--bg-light) 0%, #eeeeee 45%, var(--bg-light) 100%);
  }
  .brand {
    position: absolute;
    left: 22px;
    top: 22px;
    display: flex;
    align-items: center;
    gap: 22px;
  }
  .brand-square {
    width: 128px;
    height: 128px;
    background: var(--brand-blue);
    flex: none;
  }
  .brand-name {
    margin: 0;
    color: var(--brand-blue);
    font-weight: 500;
    line-height: 1;
  }
  .brand-name .line-main {
    display: block;
    font-size: 74px;
  }
  .brand-name .line-sub {
    display: block;
    font-size: 34px;
    margin-top: 14px;
  }
  .contact {
    position: absolute;
    left: 780px;
    top: 16px;
    margin: 0;
    padding: 0;
    list-style: none;
  }
  .contact-item {
    display: flex;
    align-items: center;
    gap: 14px;
    height: 44px;
    font-style: italic;
    font-weight: 500;
    font-size: 34px;
  }
  .contact-item + .contact-item { margin-top: 4px; }
  .contact-icon { width: 36px; height: 36px; flex: none; }
  .contact-email { color: var(--text-grey); }
  .contact-phone { color: var(--phone-blue); }
</style>
</head>
<body>
  <header class="banner">
    <div class="banner-backdrop" role="img" aria-label="Soft faded background of a gold and grey compass face"></div>

    <div class="brand">
      <div class="brand-square"></div>
      <h1 class="brand-name">
        <span class="line-main">Bayhill Trust</span>
        <span class="line-sub">West Advisors, Inc.</span>
      </h1>
    </div>

    <ul class="contact">
      <li class="contact-item contact-email">
        <svg class="contact-icon" viewBox="0 0 36 36" aria-hidden="true">
          <circle cx="18" cy="18" r="18" fill="var(--icon-dark)"/>
          <rect x="9" y="12" width="18" height="12" rx="1.5" fill="none" stroke="#ffffff" stroke-width="2"/>
          <path d="M9.5 12.5 L18 19 L26.5 12.5" fill="none" stroke="#ffffff" stroke-width="2"/>
        </svg>
        <span>info@bhtlwest.com</span>
      </li>
      <li class="contact-item contact-phone">
        <svg class="contact-icon" viewBox="0 0 36 36" aria-hidden="true">
          <circle cx="18" cy="18" r="18" fill="var(--icon-light)"/>
          <path d="M12.5 9.5 l3.5 -0.5 l2 5 l-2.5 1.8 a12 12 0 0 0 5.2 5.2 l1.8 -2.5 l5 2 l-0.5 3.5 a2 2 0 0 1 -2 1.5 A17 17 0 0 1 11 11.5 a2 2 0 0 1 1.5 -2 z" fill="#ffffff"/>
        </svg>
        <span>555-219-0387</span>
      </li>
    </ul>
  </header>
</body>
</html>
```